Business Card and Letterhead for Vantage Psychology

We need a business card design and letterhead to use for our Psychology firm that specializes in psychoeducational assessments and individual therapy. Our motto is Purpose-Driven Assessments, Meaning-Centered Therapy.Our contact information is as follows:
Vantage Psychology
The Marwick Block - 6127-48St.
Box 2716 Fernbrook, NS
T2K 3M8
t 403.555.0148 (VANT)
f 403.555.0172
www.vantagepsychology-example.ca
The business card will be used for two different psychologists so I can supply names nearer to completion. We prefer clean, uncluttered looks.

Target Market(s)

Clients, Educators

Font styles to use
Sans Serif

Colors

Designer to choose colors to be used in the design.

Requirements
Must have
• All relevant contact info, logo, some "white" space.
Nice to have
• It would be nice to see letterhead options that have the logo on the top of the page but also options that have it on the side. I think top of the page is probably our preference.
Should not have
• Too much clutter!

```html
<!DOCTYPE html>
<html lang="en">
<head>
<meta charset="utf-8">
<title>Vantage Psychology – Business Card</title>
<link href="https://fonts.googleapis.com/css2?family=Montserrat:wght@400;500;600;700&display=swap" rel="stylesheet">
<style>
  :root {
    --sky: #55c3e2;
    --sky-deep: #45b4d6;
    --amber: #f5ac3c;
    --ink: #3a3a3a;
    --paper: #ffffff;
    --backdrop: #d9d8d5;
  }
  * { box-sizing: border-box; margin: 0; padding: 0; }
  html, body { width: 1200px; height: 801px; overflow: hidden; }
  body {
    background: var(--backdrop);
    font-family: "Montserrat", Arial, sans-serif;
    display: flex; align-items: center; justify-content: center; gap: 40px;
  }
  .card {
    width: 540px; height: 308px; position: relative; overflow: hidden;
    box-shadow: 0 10px 24px rgba(0,0,0,.18);
  }
  /* Front */
  .card-front { background: var(--paper); }
  .edge-band { position: absolute; left: 0; right: 0; bottom: 0; height: 8px; display: flex; }
  .edge-band .band-sky { flex: 0 0 55%; background: var(--sky); }
  .edge-band .band-amber { flex: 1; background: var(--amber); }
  .brand {
    position: absolute; left: 36px; top: 58px; width: 170px;
    display: flex; flex-direction: column; align-items: center; gap: 14px;
  }
  .brand-dot { width: 62px; height: 62px; border-radius: 50%; background: var(--sky); }
  .brand-name {
    font-weight: 500; color: var(--sky); font-size: 15px; letter-spacing: 1.5px;
    text-align: center; line-height: 1.2;
  }
  .divider {
    position: absolute; left: 222px; top: 38px; width: 2px; height: 150px;
    background: var(--sky);
  }
  .details { position: absolute; left: 244px; top: 36px; }
  .person-name { font-weight: 700; color: var(--sky); font-size: 23px; letter-spacing: .5px; }
  .person-role { font-weight: 600; color: var(--amber); font-size: 16px; margin-bottom: 10px; }
  .contact-list { list-style: none; }
  .contact-list li {
    display: flex; align-items: center; gap: 8px;
    font-size: 11.5px; color: var(--ink); line-height: 19px;
  }
  .contact-list svg { width: 12px; height: 12px; flex: none; fill: var(--amber); }
  .contact-list .tag { color: var(--sky); }
  .company-name {
    position: absolute; left: 244px; top: 222px;
    color: var(--sky); font-size: 13px; font-weight: 500;
  }
  .company-address {
    position: absolute; left: 56px; top: 252px; white-space: nowrap;
    color: var(--ink); font-size: 12px;
  }
  /* Back */
  .card-back {
    background: linear-gradient(160deg, var(--sky) 0%, var(--sky-deep) 100%);
    display: flex; flex-direction: column; align-items: center; justify-content: center;
    color: var(--paper);
  }
  .back-dot { width: 86px; height: 86px; border-radius: 50%; background: var(--paper); margin-bottom: 20px; }
  .back-name { font-weight: 500; font-size: 27px; letter-spacing: 3px; }
  .back-web { font-size: 11px; letter-spacing: 3px; margin-top: 12px; }
</style>
</head>
<body>
  <section class="card card-front">
    <div class="brand">
      <div class="brand-dot"></div>
      <div class="brand-name">VANTAGE<br>PSYCHOLOGY</div>
    </div>
    <div class="divider"></div>
    <div class="details">
      <div class="person-name">DANIEL HARLOW</div>
      <div class="person-role">President</div>
      <ul class="contact-list">
        <li>
          <svg viewBox="0 0 24 24"><path d="M6.6 10.8a15.1 15.1 0 0 0 6.6 6.6l2.2-2.2a1 1 0 0 1 1-.25 11.4 11.4 0 0 0 3.6.57 1 1 0 0 1 1 1V20a1 1 0 0 1-1 1A17 17 0 0 1 3 4a1 1 0 0 1 1-1h3.5a1 1 0 0 1 1 1c0 1.25.2 2.45.57 3.57a1 1 0 0 1-.25 1z"/></svg>
          403.555.0172
        </li>
        <li>
          <svg viewBox="0 0 24 24"><path d="M3 9c2-4 16-4 18 0l-1 3h-4l-1-2H9l-1 2H4zM6 13h12l2 8H4zm6 2a2.5 2.5 0 1 0 0 5 2.5 2.5 0 0 0 0-5z"/></svg>
          403.555.0148 <span class="tag">(VANT)</span>
        </li>
        <li>
          <svg viewBox="0 0 24 24"><path d="M2 5h20v14H2zm2 2v.5l8 5.5 8-5.5V7z"/></svg>
          info@vantagepsychology-example.ca
        </li>
        <li>
          <svg viewBox="0 0 24 24"><circle cx="12" cy="12" r="10"/></svg>
          www.vantagepsychology-example.ca
        </li>
      </ul>
    </div>
    <div class="company-name">Vantage Psychology LTD.</div>
    <div class="company-address">The Marwick Block - 6127-48St. Box 2716 Fernbrook, NS T2K 3M8</div>
    <div class="edge-band"><span class="band-sky"></span><span class="band-amber"></span></div>
  </section>

  <section class="card card-back">
    <div class="back-dot"></div>
    <div class="back-name">VANTAGE PSYCHOLOGY</div>
    <div class="back-web">www.vantagepsychology-example.ca</div>
  </section>
</body>
</html>
```